Dance Ad Re-Design- 1/2 page ad for magazine

we would like a new design for an ad for our dance company. We are open to new ideas. please feel free to check out our website for an idea of our brand. www.brightharborballet.com.
We usually like at least a few photos. We like them to be diverse with girls and boys, different ages, etc.

Target Market(s)

dancers and parents of dancers ages 18 months-17 years old

Industry/Entity Type

Dance Studio

Colors
00a990
33b8a4
87d0c7
cfeae6
ffffff
fffefc

Requirements
Must have
• all info in the original ad. photos can be changed to the ones attached or stock photos
Nice to have
• new fresh ideas

```html
<!DOCTYPE html>
<html lang="en">
<head>
<meta charset="utf-8">
<title>Bright Harbor Ballet – Half Page Ad</title>
<link rel="stylesheet" href="https://fonts.googleapis.com/css2?family=Poppins:wght@400;500;600;700;800&display=swap">
<style>
  :root {
    --teal: #5fb3b8;
    --teal-deep: #4aa6ab;
    --ink: #111111;
    --paper: #fffefc;
    --stage: #e9efee;
    --gold: #d9b24a;
    --gold-deep: #b98d2a;
    --skin: #c89a82;
  }
  html, body { margin: 0; padding: 0; }
  body {
    width: 1200px; height: 1026px; overflow: hidden;
    background: var(--stage);
    font-family: "Poppins", sans-serif; color: var(--ink);
  }
  .ad {
    position: absolute; left: 0; top: 116px;
    width: 1200px; height: 793px;
    background: var(--paper);
  }
  .ad > * { position: absolute; margin: 0; }

  .brand-name {
    left: 47px; top: 40px; width: 420px;
    font-weight: 600; font-size: 40px; line-height: 44px; letter-spacing: 6px;
    color: var(--ink);
    border-bottom: 2px solid var(--ink); padding-bottom: 10px;
  }
  .headline {
    left: 45px; top: 196px;
    font-weight: 800; font-size: 64px; line-height: 60px; letter-spacing: 0.5px;
  }
  .styles {
    left: 51px; top: 466px; width: 320px;
    display: grid; grid-template-columns: 153px 160px; row-gap: 13px;
    list-style: none; padding: 0;
  }
  .styles li span {
    display: inline-block; background: var(--teal); color: var(--ink);
    font-size: 17px; line-height: 22px; padding: 0 14px; border-radius: 11px;
  }
  .teams {
    left: 50px; top: 630px;
    font-size: 21px; line-height: 26px;
  }

  .hero { left: 400px; top: 40px; width: 420px; height: 670px; }

  .badges { left: 410px; top: 627px; width: 370px; height: 80px; }

  .band {
    top: 731px; height: 34px; width: 396px;
    background: var(--teal);
    font-weight: 700; font-size: 23px; line-height: 34px; letter-spacing: 0.5px;
  }
  .band--left { left: 0; text-align: right; padding-right: 46px; box-sizing: border-box; }
  .band--right { left: 802px; padding-left: 32px; box-sizing: border-box; }
  .award-line {
    left: 400px; width: 400px; top: 731px; text-align: center;
    font-weight: 800; font-size: 25px; line-height: 34px; letter-spacing: 0.5px;
  }

  .info { right: 44px; text-align: right; }
  .enroll { top: 36px; font-weight: 800; font-size: 50px; line-height: 56px; letter-spacing: 1px; }
  .locations { top: 96px; font-weight: 700; font-size: 19px; line-height: 22px; letter-spacing: 1.5px; color: var(--teal-deep); }
  .season { top: 148px; font-weight: 500; font-size: 18px; line-height: 21px; letter-spacing: 0.5px; }
  .boutique { top: 272px; font-weight: 700; font-size: 34px; line-height: 35px; letter-spacing: 1.5px; color: var(--teal-deep); }
  .boutique-tag { top: 362px; font-weight: 500; font-size: 18px; line-height: 21px; letter-spacing: 0.5px; }
  .contacts { top: 454px; font-weight: 500; font-size: 18px; line-height: 21px; letter-spacing: 0.5px; }
  .contacts p { margin: 0 0 28px; }
</style>
</head>
<body>
<main class="ad">
  <h1 class="brand-name">BRIGHT HARBOR BALLET</h1>

  <h2 class="headline">YOUR<br>PREMIERE<br>DANCE<br>STUDIO</h2>

  <ul class="styles">
    <li><span>Jazz</span></li><li><span>Lyrical</span></li>
    <li><span>Ballet</span></li><li><span>Acro</span></li>
    <li><span>Hip-hop</span></li><li><span>Adult Classes</span></li>
    <li><span>Tap</span></li><li><span>18 Months - Adult</span></li>
  </ul>

  <p class="teams">Performance &amp; Competitive<br>Dance Teams<br>For Girls &amp; Boys Ages 4 - 18</p>

  <svg class="hero" viewBox="0 0 420 670">
    <path d="M205 120 C290 110 360 160 376 240 C392 320 345 405 262 425 C180 445 90 410 62 330 C35 250 110 130 205 120 Z" fill="var(--teal)"/>
    <g role="img" aria-label="Photo of a young ballerina en pointe in a standing split, arms raised">
      <defs>
        <linearGradient id="dancerTone" x1="0" y1="0" x2="0" y2="1">
          <stop offset="0" stop-color="var(--skin)" stop-opacity="0.55"/>
          <stop offset="1" stop-color="var(--skin)" stop-opacity="0.25"/>
        </linearGradient>
      </defs>
      <rect x="135" y="20" width="150" height="640" rx="70" fill="url(#dancerTone)"/>
    </g>
  </svg>

  <svg class="badges" viewBox="0 0 370 80" role="img" aria-label="Four gold award badges, 2015 to 2018">
    <circle cx="39" cy="40" r="34" fill="var(--gold)" stroke="var(--gold-deep)" stroke-width="3"/>
    <circle cx="118" cy="40" r="34" fill="var(--gold)" stroke="var(--gold-deep)" stroke-width="3"/>
    <circle cx="253" cy="40" r="34" fill="var(--gold)" stroke="var(--gold-deep)" stroke-width="3"/>
    <circle cx="332" cy="40" r="34" fill="var(--gold)" stroke="var(--gold-deep)" stroke-width="3"/>
  </svg>

  <div class="band band--left">bhdanceboutique.com</div>
  <div class="award-line">BEST DANCE PROGRAM</div>
  <div class="band band--right">brightharborballet.com</div>

  <h2 class="info enroll">NOW ENROLLING!</h2>
  <p class="info locations">HARBOR POINT, WILLOW BEND &amp; CEDAR VIEW</p>
  <p class="info season">The 2019-20 season starts<br>July 8th! Visit our website for more<br>information and to schedule your<br>FREE trial class!</p>
  <h3 class="info boutique">BRIGHT HARBOR<br>DANCE BOUTIQUE</h3>
  <p class="info boutique-tag">The Bay Area's Premiere<br>Dance Shopping Destination!</p>
  <div class="info contacts">
    <p>(555) 210-4417<br>1412-B Marina Blvd., Port Haven</p>
    <p>(555) 318-6620<br>640 W. Lantern Way, Unit C, Cedar View</p>
    <p>(555) 472-9035<br>1410 Marina Blvd., Port Haven</p>
    <p>(555) 583-1174<br>3076 Willow Bend Rd., Port Haven</p>
  </div>
</main>
</body>
</html>
```